Powerpoint visual improvements

I need a cover page, and our beliefs page and differentiating factors page / graphic design for our presentation. For the cover page I would just like an attractive design that incorporate our architectural concept with columns and potentially our logo. For the beliefs page I just want a more attractive presentatoin of the concepts. For the differentiating factors page I want a graphic that captures the points about how we are different from competitors. I have used the attached content to date, but I think it can be improved. The text is included in the graphic and I would also like to make sure the firm logo is incorporated.

Target Market(s)

Individual and institutional investors.

Industry/Entity Type

Investment Advisory

Requirements
Must have
• Our corporate colors are generally RGB 145,148,149; 66,68,76; 0,0,153; and 0,63,127. Our logo is attached. Our primary font is Georgia. Our website is www.VorlineCP.com. The key pages are www.VorlineCP.com/beliefs and www.VorlineCP.com/value we are trying to capture in a presentation. We also need a new presentation cover. Use the website as a reference for the type of imagery we like.

```html
<!DOCTYPE html>
<html lang="en">
<head>
<meta charset="utf-8">
<title>Vorline Capital Partners – Presentation Slides</title>
<link href="https://fonts.googleapis.com/css2?family=Gelasio:wght@400;700&display=swap" rel="stylesheet">
<style>
  :root{
    --grey:#919495;
    --charcoal:#42444c;
    --royal:#000099;
    --navy:#003f7f;
    --bright:#2f3fd6;
    --paper:#ffffff;
    --mist:#e9eaeb;
    --serif:"Gelasio", Georgia, serif;
  }
  *{margin:0;padding:0;box-sizing:border-box}
  html,body{width:680px;height:1200px;overflow:hidden;background:var(--paper)}
  body{position:relative;font-family:var(--serif)}
  .slide{position:absolute;width:334px;height:188px;overflow:hidden;box-shadow:0 1px 4px rgba(0,0,0,.35);background:var(--paper)}
  .col-a{left:3px}.col-b{left:343px}
  .row-1{top:6px}.row-2{top:206px}.row-3{top:406px}.row-4{top:606px}.row-5{top:806px}.row-6{top:1006px}
  .photo{position:absolute;inset:0}

  .brand{position:absolute;display:flex;align-items:center;gap:3px;color:var(--paper);font-size:11px;line-height:1;font-weight:400}
  .brand-dot{width:20px;height:20px;border-radius:50%;background:currentColor}
  .brand.small{font-size:4px;gap:1.5px}
  .brand.small .brand-dot{width:6px;height:6px}

  .cover-title{position:absolute;color:var(--paper);font-size:16px;font-weight:400;white-space:nowrap}
  .cover-sub{position:absolute;color:var(--paper);font-size:4.5px;white-space:nowrap}

  .slide-heading{position:absolute;left:16px;top:14px;font-size:11.5px;font-weight:400;color:var(--paper)}
  .slide-heading::after{content:"";display:block;width:14px;height:1.5px;background:currentColor;margin-top:3px}
  .light .slide-heading{color:#6a6c71}

  .footer{position:absolute;left:0;right:0;bottom:0;height:9px;background:var(--grey);display:flex;align-items:center;padding:0 6px;color:var(--paper);font-size:3.3px}
  .footer .tagline{margin-left:auto;margin-right:28px}
  .footer .page{width:6px;text-align:right}

  .wheel{position:absolute;left:97px;top:34px;width:140px;height:140px}
  .wheel-light{--s:#f4f5f6;--b1:var(--bright);--b2:var(--navy);--b3:var(--royal);--b4:var(--charcoal);--b5:var(--grey);--b6:var(--bright);--label:var(--navy);--f1:var(--s);--f2:var(--s);--f3:var(--s);--f4:var(--s);--f5:var(--s);--f6:var(--s)}
  .wheel-dark{--f1:var(--charcoal);--f2:var(--navy);--f3:var(--royal);--f4:var(--charcoal);--f5:var(--grey);--f6:var(--charcoal);--b1:var(--charcoal);--b2:var(--navy);--b3:var(--royal);--b4:var(--charcoal);--b5:var(--grey);--b6:var(--charcoal);--label:var(--paper)}

  .belief-wheel{position:absolute;left:97px;top:24px;width:136px;height:136px}
  .belief{position:absolute;width:80px;font-size:3.2px;line-height:1.35;color:#55575c}
  .belief h3{font-size:4px;font-weight:700;margin-bottom:1px}
  .belief.cost h3,.belief.research h3{color:var(--royal)}
  .belief.access,.belief.focus{text-align:right}
  .belief.access h3,.belief.focus h3{color:#55575c}

  .band{position:absolute;display:flex;align-items:center}
  .divider-title{color:var(--paper);font-size:14.5px;font-weight:400;white-space:nowrap}
  .mark-box{display:flex;align-items:center;justify-content:center}
  .mark-box span{width:18px;height:18px;border-radius:50%;background:var(--paper)}
</style>
</head>
<body>

<svg width="0" height="0" style="position:absolute" aria-hidden="true">
  <defs>
    <path id="seg" d="M30.02,-15.96 L52.98,-28.17 A60,60 0 0 1 52.98,28.17 L30.02,15.96 A34,34 0 0 0 30.02,-15.96Z"/>
    <path id="band" d="M30.02,-15.96 L34.43,-18.31 A39,39 0 0 1 34.43,18.31 L30.02,15.96 A34,34 0 0 0 30.02,-15.96Z"/>
    <path id="quad" d="M22.29,-20.07 L46.07,-41.48 A62,62 0 0 1 46.07,41.48 L22.29,20.07 A30,30 0 0 0 22.29,-20.07Z"/>
    <g id="difference-wheel">
      <g stroke="#d5d7d9" stroke-width=".5">
        <use href="#seg" transform="rotate(-120)" style="fill:var(--f1)"/>
        <use href="#seg" transform="rotate(-60)" style="fill:var(--f2)"/>
        <use href="#seg" style="fill:var(--f3)"/>
        <use href="#seg" transform="rotate(60)" style="fill:var(--f4)"/>
        <use href="#seg" transform="rotate(120)" style="fill:var(--f5)"/>
        <use href="#seg" transform="rotate(180)" style="fill:var(--f6)"/>
      </g>
      <use href="#band" transform="rotate(-120)" style="fill:var(--b1)"/>
      <use href="#band" transform="rotate(-60)" style="fill:var(--b2)"/>
      <use href="#band" style="fill:var(--b3)"/>
      <use href="#band" transform="rotate(60)" style="fill:var(--b4)"/>
      <use href="#band" transform="rotate(120)" style="fill:var(--b5)"/>
      <use href="#band" transform="rotate(180)" style="fill:var(--b6)"/>
      <circle r="27" fill="#f4f5f6" stroke="#d5d7d9" stroke-width="1"/>
      <circle r="15" fill="#919495"/>
      <g fill="#ffffff" stroke="#c9cbcd" stroke-width=".5">
        <circle cx="-31" cy="-53.7" r="5"/><circle cx="31" cy="-53.7" r="5"/>
        <circle cx="62" cy="0" r="5"/><circle cx="31" cy="53.7" r="5"/>
        <circle cx="-31" cy="53.7" r="5"/><circle cx="-62" cy="0" r="5"/>
      </g>
      <g fill="#003f7f">
        <circle cx="-31" cy="-53.7" r="1.8"/><circle cx="31" cy="-53.7" r="1.8"/>
        <circle cx="62" cy="0" r="1.8"/><circle cx="31" cy="53.7" r="1.8"/>
        <circle cx="-31" cy="53.7" r="1.8"/><circle cx="-62" cy="0" r="1.8"/>
      </g>
      <g font-family="Gelasio, Georgia, serif" font-size="4" text-anchor="middle" style="fill:var(--label)">
        <text transform="translate(-22.5,-38.97) rotate(-30)"><tspan x="0" y="-1">Transparent</tspan><tspan x="0" y="4">Communication</tspan></text>
        <text transform="translate(22.5,-38.97) rotate(30)"><tspan x="0" y="-1">Experienced</tspan><tspan x="0" y="4">Investors</tspan></text>
        <text transform="translate(45,0) rotate(90)"><tspan x="0" y="-1">Independent Portfolio</tspan><tspan x="0" y="4">Construction</tspan></text>
        <text transform="translate(22.5,38.97) rotate(-30)"><tspan x="0" y="-1">Sound Operational</tspan><tspan x="0" y="4">Platform</tspan></text>
        <text transform="translate(-22.5,38.97) rotate(30)"><tspan x="0" y="-1">Proactive Total Fee</tspan><tspan x="0" y="4">Management</tspan></text>
        <text transform="translate(-45,0) rotate(90)"><tspan x="0" y="-1">Institutional</tspan><tspan x="0" y="4">Research Process</tspan></text>
      </g>
    </g>
  </defs>
</svg>

<!-- Cover A -->
<section class="slide col-a row-1">
  <div class="photo" role="img" aria-label="Photograph of a colonnade corridor with columns in shadow" style="background:linear-gradient(120deg,#9a9c9f 0%,#5d5f64 45%,#4e5055 70%,#77797d 100%)"></div>
  <div class="brand" style="right:15px;top:24px"><span class="brand-dot"></span>Vorline</div>
  <h1 class="cover-title" style="right:17px;top:134px">Your Title Goes Here</h1>
  <p class="cover-sub" style="right:17px;top:157px">Your Subtitle Goes Here</p>
</section>

<!-- Cover B -->
<section class="slide col-b row-1">
  <div class="photo" role="img" aria-label="Photograph of classical fluted column bases" style="background:linear-gradient(100deg,#b9b4a8 0%,#8c8a86 30%,#7e8084 60%,#9a9c9f 100%)"></div>
  <div class="brand" style="right:15px;top:24px"><span class="brand-dot"></span>Vorline</div>
  <h1 class="cover-title" style="right:17px;top:134px">Your Title Goes Here</h1>
  <p class="cover-sub" style="right:17px;top:157px">Your Subtitle Goes Here</p>
</section>

<!-- Cover C -->
<section class="slide col-a row-2">
  <div class="photo" role="img" aria-label="Photograph of a sunlit arcade with columns casting striped shadows" style="background:linear-gradient(90deg,#55575c 0%,#6b6d71 45%,#a19d94 75%,#7b7c80 100%)"></div>
  <div class="brand" style="left:18px;top:24px"><span class="brand-dot"></span>Vorline</div>
  <h1 class="cover-title" style="left:24px;top:115px">Your Title Goes Here</h1>
  <p class="cover-sub" style="left:119px;top:138px">Your Subtitle Goes Here</p>
</section>

<!-- Cover D -->
<section class="slide col-b row-2">
  <div class="photo" role="img" aria-label="Photograph of a polished marble hall with columns" style="background:linear-gradient(160deg,#a5a7a9 0%,#8e9093 50%,#9c9ea0 100%)"></div>
  <div class="brand" style="left:18px;top:24px"><span class="brand-dot"></span>Vorline</div>
  <h1 class="cover-title" style="left:18px;top:131px">Your Title Goes Here</h1>
  <p class="cover-sub" style="left:18px;top:152px">Your Subtitle Goes Here</p>
</section>

<!-- Difference: grey -->
<section class="slide col-a row-3">
  <div class="photo" role="img" aria-label="Faded photograph of columns in soft grey" style="background:linear-gradient(90deg,#8c8e91 0%,#6f7175 60%,#8a8c8f 100%)"></div>
  <h2 class="slide-heading">The Vorline Difference</h2>
  <svg class="wheel wheel-light" viewBox="-70 -70 140 140" role="img" aria-label="Six ways Vorline differs"><use href="#difference-wheel"/></svg>
  <footer class="footer"><span class="brand small" style="position:static"><span class="brand-dot"></span>Vorline</span><span class="tagline">Vorline Capital Partners is an investment advisor founded by investors.</span><span class="page">5</span></footer>
</section>

<!-- Difference: light -->
<section class="slide col-b row-3 light">
  <div class="photo" role="img" aria-label="Very faint photograph of columns on white" style="background:linear-gradient(90deg,#fbfbfb 0%,#f0f1f2 60%,#e4e5e6 100%)"></div>
  <h2 class="slide-heading">The Vorline Difference</h2>
  <svg class="wheel wheel-dark" viewBox="-70 -70 140 140" role="img" aria-label="Six ways Vorline differs"><use href="#difference-wheel"/></svg>
  <footer class="footer"><span class="brand small" style="position:static"><span class="brand-dot"></span>Vorline</span><span class="tagline">Vorline Capital Partners is an investment advisor founded by investors.</span><span class="page">6</span></footer>
</section>

<!-- Difference: blue -->
<section class="slide col-a row-4">
  <div class="photo" style="background:linear-gradient(120deg,#1a2bd0 0%,#0a1aa8 45%,#003f7f 100%)"></div>
  <h2 class="slide-heading">The Vorline Difference</h2>
  <svg class="wheel wheel-light" viewBox="-70 -70 140 140" role="img" aria-label="Six ways Vorline differs"><use href="#difference-wheel"/></svg>
  <footer class="footer"><span class="brand small" style="position:static"><span class="brand-dot"></span>Vorline</span><span class="tagline">Vorline Capital Partners is an investment advisor founded by investors.</span><span class="page">7</span></footer>
</section>

<!-- Our Beliefs -->
<section class="slide col-b row-4 light">
  <div class="photo" role="img" aria-label="Very faint photograph of columns on white" style="background:linear-gradient(90deg,#ffffff 0%,#f3f4f5 100%)"></div>
  <h2 class="slide-heading">Our Beliefs</h2>
  <svg class="belief-wheel" viewBox="-68 -68 136 136" role="img" aria-label="Four beliefs around a central circle">
    <g stroke="#ffffff" stroke-width="1.5">
      <use href="#quad" transform="rotate(-90)" fill="#000099"/>
      <use href="#quad" fill="#003f7f"/>
      <use href="#quad" transform="rotate(90)" fill="#42444c"/>
      <use href="#quad" transform="rotate(180)" fill="#919495"/>
    </g>
    <circle r="24" fill="#f4f5f6" stroke="#d5d7d9"/>
    <circle r="14" fill="#919495"/>
    <g fill="none" stroke="#ffffff" stroke-width="1.6">
      <circle cx="0" cy="-45" r="5"/>
      <rect x="40" y="-6" width="9" height="12" rx="1"/>
      <circle cx="0" cy="45" r="5"/><circle cx="0" cy="45" r="1.5"/>
      <path d="M-49,-4 h6 M-49,0 h8 M-49,4 h6"/>
    </g>
    <g stroke="#919495" stroke-width=".4" fill="none">
      <path d="M38,-52 L58,-58"/>
    </g>
  </svg>
  <div class="belief cost" style="left:234px;top:33px"><h3>Cost Matters</h3>We believe investors pay too much for advice. Lower costs compound over time, so our fees are built to stay below industry norms.</div>
  <div class="belief research" style="left:248px;top:105px"><h3>Research Matters</h3>We believe thorough research drives results. Our founders bring decades of investment experience and we run all research in house.</div>
  <div class="belief access" style="left:4px;top:72px"><h3>Access Matters</h3>We believe everyone should have access to skilled investment management. Our minimums, fees and portfolios reflect this conviction.</div>
  <div class="belief focus" style="left:30px;top:141px"><h3>Focus Matters</h3>We stay focused on what we do best: building disciplined portfolios with clear goals and steady, long term thinking.</div>
  <footer class="footer"><span class="brand small" style="position:static"><span class="brand-dot"></span>Vorline</span><span class="tagline">Vorline Capital Partners is an investment advisor founded by investors.</span><span class="page">8</span></footer>
</section>

<!-- Divider: blue band -->
<section class="slide col-a row-5">
  <div class="photo" role="img" aria-label="Photograph of bright classical columns in sunlight" style="background:linear-gradient(90deg,#6e7073 0%,#c9c8c4 35%,#a7a7a6 70%,#8a8b8d 100%)"></div>
  <div class="band" style="left:0;right:0;top:106px;bottom:0;background:rgba(0,63,127,.88)"></div>
  <div class="brand" style="left:19px;top:128px;font-size:8px"><span class="brand-dot" style="width:14px;height:14px"></span>Vorline</div>
  <h2 class="divider-title" style="position:absolute;left:20px;top:148px">This Is Your Divider Page</h2>
</section>

<!-- Divider: diagonal -->
<section class="slide col-b row-5">
  <div class="photo" role="img" aria-label="Faint photograph of columns behind a diagonal panel" style="clip-path:polygon(33% 0,100% 0,100% 100%,70% 100%);background:linear-gradient(180deg,#e6e7e8 0%,#d9dadb 100%)"></div>
  <div class="band" style="left:0;right:0;top:84px;height:30px;background:rgba(145,148,149,.85)">
    <div class="mark-box" style="width:40px;height:30px;background:var(--charcoal)"><span></span></div>
    <h2 class="divider-title" style="margin-left:20px">This Is Your Divider Page</h2>
  </div>
</section>

<!-- Divider: white lower -->
<section class="slide col-a row-6">
  <div class="photo" role="img" aria-label="Faded photograph of a colonnade" style="bottom:82px;background:linear-gradient(90deg,#a3a5a7 0%,#8f9194 100%)"></div>
  <div class="band" style="left:0;right:0;top:106px;height:6px;background:var(--charcoal)"></div>
  <div class="brand" style="left:15px;top:127px;font-size:12px;color:var(--grey)"><span class="brand-dot" style="width:22px;height:22px"></span>Vorline</div>
  <h2 class="divider-title" style="position:absolute;left:15px;top:155px;color:var(--grey);font-size:15px">This Is Your Divider Page</h2>
</section>

<!-- Divider: dark band -->
<section class="slide col-b row-6">
  <div class="photo" role="img" aria-label="Faded photograph of a colonnade corridor" style="background:linear-gradient(90deg,#b0b2b4 0%,#9c9ea0 50%,#a9abad 100%)"></div>
  <div class="band" style="left:0;width:301px;top:122px;height:32px;background:rgba(66,68,76,.92)">
    <div class="mark-box" style="width:40px;height:32px;background:#5d5f66"><span></span></div>
    <h2 class="divider-title" style="margin-left:11px">This Is Your Divider Page</h2>
  </div>
</section>

</body>
</html>
```